Business Card Design needed for logo design project

Our business needs a business card design. I'm not sure what format files are generally delivered back, but clearly I will need the ability to edit to add colleagues contact details.

Our logo is attached.

Brivanor is a 3D design services company, providing app, serious/educational game, VR and AR websites/applications to corporate clients.

Target Market(s)

Corporate blue-chip clients needing 3D design services

Industry/Entity Type

Business

Font styles to use
Sans Serif

Requirements
Must have
• Templated such that I can add details (name, phone number etc). Needs to include logo from previous project winner - attached.

```html
<!DOCTYPE html>
<html lang="en">
<head>
<meta charset="utf-8">
<title>Brivanor Business Card</title>
<link rel="stylesheet" href="https://fonts.googleapis.com/css2?family=Questrial&family=Mulish:wght@400;800&display=swap">
<style>
  :root {
    --brand-red: #e61e2a;
    --ink: #3a3a3a;
    --paper: #ffffff;
    --backdrop: #6f6a67;
  }
  * { margin: 0; padding: 0; box-sizing: border-box; }
  html, body { width: 1200px; height: 1000px; overflow: hidden; }
  body {
    position: relative;
    background: var(--backdrop);
    font-family: "Mulish", sans-serif;
  }
  .card {
    position: absolute;
    left: 265px;
    width: 667px;
    height: 397px;
    overflow: hidden;
  }
  .card--front { top: 73px; background: var(--brand-red); }
  .card--back { top: 533px; background: var(--paper); }

  .feature-circle {
    position: absolute;
    border-radius: 50%;
  }
  .card--front .feature-circle {
    left: 3px; top: 42px; width: 310px; height: 310px;
    background: var(--paper);
  }
  .card--back .feature-circle {
    left: 348px; top: 37px; width: 320px; height: 320px;
    background: var(--brand-red);
  }

  .wordmark {
    position: absolute;
    font-family: "Questrial", sans-serif;
    font-weight: 400;
    letter-spacing: 1px;
    line-height: 1;
  }
  .card--front .wordmark {
    left: 347px; top: 172px;
    font-size: 58px;
    color: var(--paper);
  }
  .brand-lockup {
    position: absolute;
    left: 22px; top: 17px;
    display: flex; align-items: center; gap: 8px;
  }
  .brand-lockup .dot {
    width: 66px; height: 66px; border-radius: 50%;
    background: var(--brand-red);
  }
  .brand-lockup .wordmark {
    position: static;
    font-size: 50px;
    color: var(--ink);
  }

  .person { position: absolute; left: 22px; top: 139px; }
  .person__name {
    font-weight: 800; font-size: 22px; letter-spacing: 0.5px;
    color: var(--brand-red); line-height: 1.1;
  }
  .person__title { font-size: 17px; color: var(--ink); margin-top: 3px; }

  .contact {
    position: absolute; left: 22px;
    list-style: none;
    font-size: 17px; color: var(--ink);
  }
  .contact li { display: flex; align-items: center; height: 26px; }
  .contact svg { width: 14px; height: 14px; margin-right: 10px; fill: var(--brand-red); flex: none; }
  .contact--phones { top: 209px; }
  .contact--web { top: 294px; }
  .contact--place { top: 350px; }
</style>
</head>
<body>

<section class="card card--front">
  <div class="feature-circle"></div>
  <div class="wordmark">BRIVANOR</div>
</section>

<section class="card card--back">
  <div class="brand-lockup">
    <div class="dot"></div>
    <div class="wordmark">BRIVANOR</div>
  </div>

  <div class="feature-circle"></div>

  <div class="person">
    <div class="person__name">TOBIN HALVARSEN</div>
    <div class="person__title">Executive Director</div>
  </div>

  <ul class="contact contact--phones">
    <li><svg viewBox="0 0 14 14"><path d="M4 0h6a1 1 0 0 1 1 1v12a1 1 0 0 1-1 1H4a1 1 0 0 1-1-1V1a1 1 0 0 1 1-1zm0.5 1.5v10h5v-10z"/></svg>+61 400 555 218</li>
    <li><svg viewBox="0 0 14 14"><path d="M1 5c0-2 3-3 6-3s6 1 6 3v1h-3V4.5H4V6H1zM3 7h8l2 6H1z"/></svg>+61 3 5550 1234</li>
    <li><svg viewBox="0 0 14 14"><path d="M3 0h8v4H3zM0 5h14v6h-3v3H3v-3H0zm4 4v4h6V9z"/></svg>+61 3 5550 4871</li>
  </ul>

  <ul class="contact contact--web">
    <li><svg viewBox="0 0 14 14"><path d="M0 3h14v1L7 8 0 4zm0 2.5 7 4 7-4V12H0z"/></svg>tobin@brivanor.com</li>
    <li><svg viewBox="0 0 14 14"><path d="M7 0a7 7 0 1 0 0 14A7 7 0 0 0 7 0zm-1 1.3v2.2H3.2A5.7 5.7 0 0 1 6 1.3zm2 0a5.7 5.7 0 0 1 2.8 2.2H8zM1.4 6h4.6v2H1.4zm6.6 0h4.6v2H8zm-4.8 4.5H6v2.2a5.7 5.7 0 0 1-2.8-2.2zm4.8 0h2.8A5.7 5.7 0 0 1 8 12.7z"/></svg>www.brivanor.com</li>
  </ul>

  <ul class="contact contact--place">
    <li><svg viewBox="0 0 14 14"><path d="M7 0a5 5 0 0 1 5 5c0 3.5-5 9-5 9S2 8.5 2 5a5 5 0 0 1 5-5zm0 3a2 2 0 1 0 0 4 2 2 0 0 0 0-4z"/></svg>14 Larkhill Road Ferngrove VIC 3999</li>
  </ul>
</section>

</body>
</html>
```